Sneaker Company looking for a partner on multiple packaging designs!

We are a company who is passionate about Sneakers and quality products! This project is the first of many packaging designs we will need. We have our logo (see attached) and we would like the background to be all black for this package. I'm working on the UPC number right now so please leave a space for the UPC. Where we need some help is the overall design and some "marketing" word smithing. We are hoping to find a partner that we can work with on future products as well who really understands us and our products! Our company name is Kolvu and this first product will be for crease protection. They are known at Crease Guards, Crease Protection, Anti-Crease Inserts, etc...Not sure the right name to go with but would love some feedback! The package will have 2 Pairs inside. (One Black and One white). This product is something you slide into the shoe while you are wearing it. This product helps prevent the creasing of the toe box. Basically to help keep the sneaker clean and crisp! They are labeled L and R for Left and Right. They are also thin enough that you can trim them with scissors to fit! I have much more to share but before adding all the marketing words, if this is a project you would like to take on please message me and let’s chat! I want to make sure this is a good fit for both of us. Please do not submit projects without speaking to me first. If doing so that means you didn’t read this and you will immediately be removed from contention.

Thank you and look forward to working with you!
Marcus

Target Market(s)

Customers who love Sneakers

Industry/Entity Type

Retail

Font styles to use
Sans Serif

Requirements
Must have
• Clean, Original and Simple
Nice to have
• Pretty open!
Should not have
• Anything copied from another product. No more than 4 colors total on the box.

```html
<!DOCTYPE html>
<html lang="en">
<head>
<meta charset="utf-8">
<title>Kolvu Crease Guards – Lid</title>
<link rel="stylesheet" href="https://fonts.googleapis.com/css2?family=Titan+One&family=Montserrat:wght@400;600&display=swap">
<style>
  :root {
    --stage: #f1f1f1;
    --box-black: #0b0b0b;
    --mint: #3ec497;
    --mint-soft: rgba(62, 196, 151, 0.55);
    --slate: #67666b;
    --slate-soft: rgba(103, 102, 107, 0.45);
    --white: #ffffff;
    --figure: #3a3a3a;
  }
  * { margin: 0; padding: 0; box-sizing: border-box; }
  html, body { width: 1200px; height: 847px; overflow: hidden; background: var(--stage); }
  .lid {
    position: absolute; left: 80px; top: 113px;
    width: 1040px; height: 620px;
    background: var(--box-black);
    border-radius: 22px;
    overflow: hidden;
  }
  .stripe-graphic {
    position: absolute; left: 0; top: 300px;
    width: 560px; height: 320px;
    background:
      radial-gradient(ellipse at 40% 60%, var(--mint-soft), transparent 62%),
      radial-gradient(ellipse at 70% 80%, var(--slate-soft), transparent 65%);
  }
  .brand {
    position: absolute; left: 64px; top: 44px;
    display: flex; align-items: center; gap: 14px;
    font-family: "Montserrat", sans-serif; font-weight: 600;
    font-size: 46px; letter-spacing: 3px; color: var(--slate);
  }
  .brand-dot { width: 16px; height: 16px; background: var(--mint); }
  .athlete {
    position: absolute; left: 60px; top: 120px;
    width: 250px; height: 300px;
    background: radial-gradient(ellipse at 55% 45%, var(--figure), transparent 70%);
  }
  .headline {
    position: absolute; right: 70px; top: 230px;
    text-align: right;
    font-family: "Titan One", sans-serif;
  }
  .tagline {
    display: inline-block;
    background: var(--mint); color: var(--box-black);
    font-size: 30px; line-height: 1;
    padding: 8px 22px;
    border-radius: 4px;
  }
  .title-line1 { color: var(--white); font-size: 74px; line-height: 1; margin-top: 10px; }
  .title-line2 { color: var(--mint); font-size: 100px; line-height: 0.95; }
  .subtitle {
    position: absolute; right: 70px; top: 478px;
    font-family: "Montserrat", sans-serif; font-weight: 400;
    font-size: 30px; color: var(--slate); letter-spacing: 1px;
  }
  .size {
    position: absolute; right: 70px; top: 526px;
    font-family: "Titan One", sans-serif; font-size: 44px; color: var(--mint);
  }
  .size b { color: var(--white); font-weight: 400; margin-left: 14px; }
</style>
</head>
<body>
  <main class="lid">
    <div class="stripe-graphic" role="img" aria-label="Mint and grey angled stripe graphic"></div>
    <div class="brand"><span>kolvu</span><span class="brand-dot"></span></div>
    <div class="athlete" role="img" aria-label="Grey silhouette of a jumping sneaker wearer"></div>
    <div class="headline">
      <span class="tagline">Maximum Comfort</span>
      <div class="title-line1">Crease</div>
      <div class="title-line2">Guards</div>
    </div>
    <div class="subtitle">Shoe Crease Protectors</div>
    <div class="size">Size<b>L</b></div>
  </main>
</body>
</html>
```